Conversion Optimisation Checklist for eCommerce websites

We need a design for a 2 page pdf checklist (attached document outline), the first page is checklist. Document will be primarly for digital viewing - don't need to worry about print. Should have our website address (brozzo.com.au), email (hello@brozzo.com.au) and phone number (1300 418 907) in the footer
The second page is a bonus, a wireframe of an ecommerce homepage with annotations to show what information is important where.
Should be branded with our branding (logo attached) and compliment the design (colours/style/imagery) of an accompanying landing page design (attached).

We are a website and marketing agency thank helps young ecommerce businesses to grow faster.

Industry/Entity Type

Digital

```html
<!DOCTYPE html>
<html lang="en">
<head>
<meta charset="utf-8">
<title>Brozzo Interactive – 25-Step Conversion Checklist</title>
<link href="https://fonts.googleapis.com/css2?family=Montserrat:wght@400;500;600;700;800&family=Permanent+Marker&display=swap" rel="stylesheet">
<style>
  :root{
    --stage:#6e6e6e;
    --navy:#0f1e33;
    --navy-2:#2b4656;
    --blue:#3a8fd6;
    --blue-dark:#2f7fc4;
    --ink:#3a3f45;
    --muted:#6b7278;
    --panel:#ebedef;
    --block:#cfd2d5;
    --paper:#ffffff;
    --foot:#f0f1f2;
  }
  *{box-sizing:border-box;margin:0;padding:0}
  html,body{width:1200px;height:890px;overflow:hidden;background:var(--stage);font-family:"Montserrat",sans-serif;color:var(--ink)}
  .page{position:absolute;top:84px;width:514px;height:726px;background:var(--paper);overflow:hidden;box-shadow:0 2px 8px rgba(0,0,0,.25)}
  .page--checklist{left:66px}
  .page--wireframe{left:626px}

  /* header */
  .hero{position:absolute;left:0;top:0;width:514px;height:230px;background:linear-gradient(120deg,var(--navy) 40%,var(--navy-2))}
  .hero-band{position:absolute;left:0;top:190px}
  .brand{position:absolute;display:flex;align-items:center;gap:6px;font-weight:800;letter-spacing:.5px}
  .brand-dot{width:14px;height:14px;border-radius:50%;background:var(--blue)}
  .hero .brand{left:40px;top:38px;color:#fff;font-size:18px}
  .steps-title{position:absolute;left:40px;top:100px;font-family:"Permanent Marker","Montserrat",sans-serif;font-size:38px;color:var(--blue);line-height:1}
  .hero-sub{position:absolute;left:41px;top:148px;color:#fff;font-weight:700;font-size:13.6px;line-height:17px}
  .device-art{position:absolute;left:354px;top:70px;width:160px;height:143px;border-radius:4px;background:linear-gradient(160deg,#f4f5f6,#d9dcdf)}

  /* checklist */
  .section-title{position:absolute;font-weight:700;font-size:13.5px;color:var(--blue);line-height:15px;white-space:nowrap}
  .section-rule{position:absolute;height:1px;background:var(--blue)}
  .section-rule::before{content:"";position:absolute;left:-1px;top:-1.5px;width:4px;height:4px;border-radius:50%;background:var(--blue)}
  .item{position:absolute;font-size:8.8px;line-height:10.4px;color:var(--ink);width:170px}
  .item::before{content:"";position:absolute;left:-24px;top:1px;width:14px;height:14px;border-radius:50%;border:1.3px solid var(--blue)}
  .item::after{content:"";position:absolute;left:-20px;top:5.5px;width:4px;height:4px;border-top:1.3px solid var(--blue);border-right:1.3px solid var(--blue);transform:rotate(45deg)}
  .foot-band{position:absolute;left:0;bottom:0}

  /* wireframe page */
  .wire{position:absolute;left:0;top:0}
  .wire text{font-family:"Montserrat",sans-serif;font-size:8px;fill:var(--muted)}
  .wire .contact{font-size:10px;font-weight:700;fill:var(--blue)}
  .wire .brand-text{font-size:15px;font-weight:800;fill:var(--navy)}
</style>
</head>
<body>

<section class="page page--checklist">
  <header class="hero">
    <div class="brand"><span class="brand-dot"></span>BROZZO</div>
    <div class="steps-title">25-STEP</div>
    <h1 class="hero-sub">Checklist to Optimise your Website<br>and Increase Sales Conversions</h1>
    <div class="device-art" role="img" aria-label="Laptop and phone showing an online store dashboard"></div>
    <svg class="hero-band" width="514" height="40" viewBox="0 0 514 40">
      <path d="M0 10 L120 6 L200 4 L300 2 L360 6 L514 2 L514 40 L0 40Z" fill="var(--blue)"/>
      <path d="M0 24 L90 18 L180 16 L260 14 L340 16 L420 10 L514 12 L514 40 L0 40Z" fill="#fff"/>
    </svg>
  </header>

  <h2 class="section-title" style="left:41px;top:258px">BE COMPELLING</h2>
  <span class="section-rule" style="left:160px;top:266px;width:58px"></span>
  <p class="item" style="left:65px;top:281px">Encourage purchases with featured products or sales</p>
  <p class="item" style="left:65px;top:308px">Draw attention to popular<br>(or profitable) products</p>
  <p class="item" style="left:65px;top:336px">Clearly show discounted pricing<br>and the benefit</p>
  <p class="item" style="left:65px;top:363px">Encourage purchases over a free<br>shipping threshold</p>
  <p class="item" style="left:65px;top:391px">Make your site messaging reflect the key benefits your products provide</p>

  <h2 class="section-title" style="left:258px;top:258px">BUILD TRUST</h2>
  <span class="section-rule" style="left:373px;top:266px;width:103px"></span>
  <p class="item" style="left:286px;top:281px;width:190px">Includes your phone number on key areas people might have questions like the cart or checkout</p>
  <p class="item" style="left:286px;top:318px">Ensure your site uses a SSL certificate<br>and loads over https</p>
  <p class="item" style="left:286px;top:346px">Offer different payment methods</p>
  <p class="item" style="left:286px;top:363px">Have a professional<br>design</p>
  <p class="item" style="left:286px;top:391px;width:200px">Have all the information customers need including shipping, returns &amp; delivery policies</p>

  <h2 class="section-title" style="left:41px;top:431px">BE SIMPLE</h2>
  <span class="section-rule" style="left:124px;top:439px;width:94px"></span>
  <p class="item" style="left:65px;top:453px">Make navigation<br>clear &amp; simple</p>
  <p class="item" style="left:65px;top:480px">Display products and their<br>price clearly</p>
  <p class="item" style="left:65px;top:508px">Have additional information for<br>products that need it</p>
  <p class="item" style="left:65px;top:535px">Use high quality images to show<br>off your product</p>
  <p class="item" style="left:65px;top:563px;width:180px">Ensure you have appropriate shipping methods setup for your customers</p>

  <h2 class="section-title" style="left:258px;top:431px">DRIVE TRAFFIC</h2>
  <span class="section-rule" style="left:374px;top:439px;width:102px"></span>
  <p class="item" style="left:286px;top:453px;width:180px">Ensure your website is setup and opti-<br>mised for search keywords</p>
  <p class="item" style="left:286px;top:480px">Ensure reporting &amp; tracking<br>is in place</p>
  <p class="item" style="left:286px;top:508px;width:180px">Consider paid marketing and measure your ROI through analytics</p>
  <p class="item" style="left:286px;top:535px">Regularly review<br>reports</p>
  <p class="item" style="left:286px;top:563px;width:180px">Build interesting and insightful content<br>around your products</p>

  <h2 class="section-title" style="left:42px;top:615px">ENGAGE YOUR<br>CUSTOMERS</h2>
  <span class="section-rule" style="left:150px;top:622px;width:18px"></span>
  <p class="item" style="left:207px;top:618px;width:140px">Email customers that abandon their cart before purchasing</p>
  <p class="item" style="left:379px;top:618px;width:110px">Reward loyal &amp; repeat customers</p>
  <p class="item" style="left:65px;top:655px;width:115px">Engage with customers on social media through related groups or pages</p>
  <p class="item" style="left:207px;top:655px;width:130px">Use email automation to follow up existing customers with offers or promotions</p>
  <p class="item" style="left:379px;top:655px;width:110px">Setup a referral bonus for new customers</p>

  <svg class="foot-band" width="514" height="40" viewBox="0 0 514 40">
    <path d="M0 30 L120 26 L260 24 L360 22 L440 16 L514 12 L514 40 L0 40Z" fill="var(--foot)"/>
    <path d="M320 24 L420 18 L514 10 L514 20 L420 24 L320 26Z" fill="var(--blue)"/>
  </svg>
</section>

<section class="page page--wireframe">
  <svg class="wire" width="514" height="726" viewBox="0 0 642 908">
    <g fill="none" stroke="#c8ccd0" stroke-width="1">
      <circle cx="153" cy="76" r="6"/><circle cx="324" cy="76" r="6"/><circle cx="475" cy="76" r="6"/>
      <circle cx="108" cy="149" r="6"/><circle cx="108" cy="176" r="6"/><circle cx="108" cy="308" r="6"/>
      <circle cx="108" cy="496" r="6"/><circle cx="108" cy="625" r="6"/><circle cx="108" cy="738" r="6"/>
      <circle cx="527" cy="104" r="6"/><circle cx="527" cy="136" r="6"/><circle cx="527" cy="236" r="6"/>
      <circle cx="527" cy="327" r="6"/><circle cx="527" cy="436" r="6"/><circle cx="527" cy="514" r="6"/>
      <circle cx="527" cy="617" r="6"/><circle cx="527" cy="667" r="6"/><circle cx="527" cy="738" r="6"/>
    </g>
    <text x="152" y="49" text-anchor="middle">Home</text><text x="152" y="59" text-anchor="middle">Page</text>
    <text x="323" y="49" text-anchor="middle">Search</text><text x="323" y="59" text-anchor="middle">Bar</text>
    <text x="447" y="49">Currency display if multicurrency or</text><text x="447" y="59">unclear to all traffic sources</text>

    <rect x="122" y="95" width="395" height="668" fill="var(--panel)"/>
    <rect x="131" y="105" width="375" height="10" fill="#e0e2e4"/>
    <rect x="131" y="122" width="51" height="25" fill="var(--block)"/>
    <rect x="274" y="122" width="92" height="25" fill="var(--block)"/>
    <rect x="443" y="122" width="63" height="25" fill="var(--block)"/>
    <rect x="131" y="157" width="375" height="18" fill="var(--block)"/>
    <rect x="144" y="200" width="132" height="17" fill="var(--blue)"/>
    <rect x="144" y="226" width="132" height="16" fill="var(--blue)"/>
    <rect x="144" y="248" width="49" height="18" fill="none" stroke="var(--blue)"/>
    <rect x="131" y="297" width="375" height="21" fill="var(--block)"/>
    <g fill="none" stroke="var(--blue)" stroke-width="1">
      <rect x="131" y="336" width="109" height="57"/><rect x="263" y="336" width="110" height="57"/><rect x="394" y="336" width="112" height="57"/>
      <rect x="131" y="421" width="88" height="65"/><rect x="131" y="503" width="88" height="64"/>
      <rect x="420" y="421" width="86" height="65"/><rect x="420" y="503" width="86" height="64"/>
      <rect x="219" y="411" width="201" height="165" fill="var(--panel)"/>
      <rect x="131" y="593" width="88" height="64"/><rect x="226" y="593" width="92" height="64"/>
      <rect x="320" y="593" width="89" height="64"/><rect x="416" y="593" width="89" height="64"/>
    </g>
    <rect x="131" y="682" width="375" height="34" fill="#e2e4e6"/>
    <rect x="131" y="729" width="82" height="19" fill="var(--block)"/>

    <g text-anchor="end">
      <text x="92" y="151">Logo</text>
      <text x="92" y="173">Simple</text><text x="92" y="183">Navigation</text><text x="92" y="193">with cart</text>
      <text x="92" y="300">Additional</text><text x="92" y="310">messaging</text><text x="92" y="320">around returns</text><text x="92" y="330">or special</text><text x="92" y="340">requirements</text>
      <text x="92" y="491">Exit intent</text><text x="92" y="501">popup</text><text x="92" y="511">with offer</text>
      <text x="92" y="591">Information</text><text x="92" y="601">about your</text><text x="92" y="611">business, why</text><text x="92" y="621">you exist and</text><text x="92" y="631">why your</text><text x="92" y="641">customers</text><text x="92" y="651">should care</text><text x="92" y="661">ideally with a</text><text x="92" y="671">video</text>
      <text x="92" y="737">Site purchase</text><text x="92" y="747">activity dialog</text>
    </g>
    <g>
      <text x="544" y="100">Promotional</text><text x="544" y="110">message bar</text>
      <text x="544" y="137">Unique message</text><text x="544" y="147">potentially free</text><text x="544" y="157">shipping or</text><text x="544" y="167">other USP of</text><text x="544" y="177">your business</text>
      <text x="544" y="210">Key image with</text><text x="544" y="220">messaging</text><text x="544" y="230">Outlining more</text><text x="544" y="240">benefits of your</text><text x="544" y="250">products</text><text x="544" y="260">And call to</text><text x="544" y="270">action</text>
      <text x="544" y="326">Core Product</text><text x="544" y="336">categories</text>
      <text x="544" y="440">Testimonial</text>
      <text x="544" y="515">Promotional</text><text x="544" y="525">product or</text><text x="544" y="535">categories</text>
      <text x="544" y="602">Top selling</text><text x="544" y="612">products or lastest</text><text x="544" y="622">to be reviewed</text><text x="544" y="632">Showing star</text><text x="544" y="642">ratings and price</text>
      <text x="544" y="661">Newsletter</text><text x="544" y="671">subscription with</text><text x="544" y="681">offer if subscribed</text>
      <text x="544" y="700">Footer with</text><text x="544" y="710">customer care</text><text x="544" y="720">information</text><text x="544" y="730">including return</text><text x="544" y="740">&amp; delivery policy</text><text x="544" y="750">Trust symbols like</text><text x="544" y="760">accepted credit</text><text x="544" y="770">cards and/or SSL</text><text x="544" y="780">secure badges</text>
    </g>

    <path d="M0 832 L140 826 L300 824 L420 818 L520 812 L642 806 L642 908 L0 908Z" fill="var(--foot)"/>
    <path d="M360 822 L480 814 L642 804 L642 816 L500 820 L380 826Z" fill="var(--blue)"/>
    <circle cx="53" cy="868" r="8" fill="var(--blue)"/>
    <text class="brand-text" x="66" y="874">BROZZO</text>
    <g fill="none" stroke="#8a9096" stroke-width="1.2">
      <rect x="253" y="865" width="15" height="11" rx="1"/><path d="M253 866 L260.5 872 L268 866"/>
      <circle cx="410" cy="871" r="7.5"/><path d="M406.5 867.5 q0 5 6 7 l1.2-1.8 -2-1.4 -1 1 q-2-1-3-3 l1-1 -1.4-2Z"/>
      <circle cx="531" cy="871" r="7.5"/><ellipse cx="531" cy="871" rx="3.2" ry="7.5"/><path d="M523.5 871 h15 M525 867 h12 M525 875 h12"/>
    </g>
    <text class="contact" x="276" y="875">hello@brozzo.com.au</text>
    <text class="contact" x="425" y="875">1300 418 907</text>
    <text class="contact" x="544" y="875">brozzo.com.au</text>
  </svg>
</section>

</body>
</html>
```